Brindle Bones Chews Pouch Design

I want a pouch design for my yak cheese dog chews. My competitor is hollow fern, see attached. I want something minimalist like that where you see that there is only 3 ingredients, Yak milk, lime juice, Himalayan salt. I want it to say 100% natural 100% organic on it. Also odor free. There has to be a big see through window on it so you can see the products inside. Here is my logo and my competitor package. The package is 13cm x 17cm x 5cm. I have 5 sizes of bags to create but same image design
Updates

Target Market(s)

Pet owners

Industry/Entity Type

Dog products

Requirements
Must have
• « SMALL » « MIN NET WT 200 g / 5 PCS » and its important the 3 ingredients mentioned and 100% natural and organic must be very visible however the window must be big
Should not have
• The ingredients in the back

```html
<!DOCTYPE html>
<html lang="en">
<head>
<meta charset="utf-8">
<title>Brindle Bones Chews – Yak Cheese Dog Chews Pouch</title>
<link rel="stylesheet" href="https://fonts.googleapis.com/css2?family=Titan+One&display=swap">
<style>
  :root {
    --page: #e2e2e2;
    --window: #e4e4e4;
    --rose: #bd5a5a;
    --teal: #137f9b;
    --ink: #2e1a1c;
    --cream: #fff6d4;
    --amber: #f7a93c;
    --olive: #3c3f26;
    --lime: #a9b83a;
    --logo-sky: #3e8fa0;
  }
  * { margin: 0; padding: 0; box-sizing: border-box; }
  html, body {
    width: 1200px; height: 675px; overflow: hidden;
    background: var(--page);
    font-family: "Titan One", "Arial Black", sans-serif;
  }
  .pouch-face {
    position: absolute; left: 360px; top: 24px;
    width: 480px; height: 627px;
    background: linear-gradient(to bottom, var(--rose) 0 404px, var(--teal) 404px 100%);
    overflow: hidden;
  }
  .pouch-face > * { position: absolute; }
  .product-window { left: 0; top: 0; width: 480px; height: 627px; }
  .title { left: 0; top: 84px; width: 480px; height: 110px; }
  .odor-badge {
    left: 34px; top: 175px; width: 75px; height: 75px; border-radius: 50%;
    background: var(--ink); color: var(--cream);
    outline: 1px dashed var(--cream); outline-offset: -5px;
    display: flex; flex-direction: column; align-items: center; justify-content: center;
    font-size: 11px; line-height: 1.1; text-align: center;
  }
  .odor-badge .odor-icon { width: 20px; height: 20px; margin-bottom: 3px; }
  .claim {
    left: 22px; padding: 3px 10px 2px;
    font-size: 22px; letter-spacing: 0.5px; white-space: nowrap;
  }
  .claim-natural { top: 434px; background: var(--olive); color: var(--cream); }
  .claim-organic { left: 33px; top: 473px; background: var(--lime); color: var(--ink); font-size: 21px; }
  .brand-mark { left: 268px; top: 300px; width: 190px; height: 215px; display: flex; flex-direction: column; align-items: center; }
  .brand-dot {
    width: 140px; height: 140px; border-radius: 50%;
    background: radial-gradient(circle at 50% 40%, #e8a64a 0 30%, var(--logo-sky) 31% 100%);
  }
  .brand-name {
    margin-top: 10px; color: var(--cream); font-size: 22px; line-height: 1.05; text-align: center;
  }
  .ingredients-heading { left: 0; top: 520px; width: 480px; height: 30px; }
  .ingredients-band {
    left: 0; top: 553px; width: 480px; height: 24px;
    background: var(--rose); color: var(--cream);
    font-size: 16px; line-height: 25px; text-align: center; letter-spacing: 0.3px;
  }
  .net-weight {
    left: 134px; top: 590px; width: 213px; height: 14px;
    background: var(--cream); color: var(--ink);
    font-size: 8.5px; line-height: 14px; text-align: center;
  }
</style>
</head>
<body>
  <main class="pouch-face">
    <svg class="product-window" viewBox="0 0 480 627" role="img" aria-label="Clear window showing the yak cheese chews inside">
      <path fill="var(--window)" d="M0,258 Q22,244 45,249 L100,250 Q128,204 165,210 Q192,190 232,200 Q282,184 332,205 Q372,210 386,240 Q410,238 420,260 Q446,254 456,275 Q470,270 480,286 L480,404 L182,404 Q160,421 130,410 Q100,398 70,404 Q40,394 20,408 Q10,402 0,406 Z"/>
    </svg>

    <svg class="title" viewBox="0 0 480 110" aria-label="Yak Cheese Dog Chews">
      <defs>
        <linearGradient id="title-fill" x1="0" y1="0" x2="0" y2="1">
          <stop offset="0.45" stop-color="var(--cream)"/>
          <stop offset="0.55" stop-color="var(--amber)"/>
        </linearGradient>
      </defs>
      <text x="240" y="58" text-anchor="middle" textLength="404" lengthAdjust="spacingAndGlyphs"
            font-family="Titan One, sans-serif" font-size="56" fill="url(#title-fill)"
            stroke="var(--ink)" stroke-width="7" stroke-linejoin="round" paint-order="stroke">YAK CHEESE</text>
      <text x="240" y="98" text-anchor="middle" textLength="244" lengthAdjust="spacingAndGlyphs"
            font-family="Titan One, sans-serif" font-size="36" fill="var(--cream)"
            stroke="var(--ink)" stroke-width="6" stroke-linejoin="round" paint-order="stroke">DOG CHEWS</text>
    </svg>

    <div class="odor-badge">
      <svg class="odor-icon" viewBox="0 0 20 20" aria-hidden="true">
        <circle cx="10" cy="10" r="9" fill="none" stroke="var(--cream)" stroke-width="1.6"/>
        <path d="M6 14 Q8 10 6 6 M10 14 Q12 10 10 6 M14 14 Q16 10 14 6" fill="none" stroke="var(--cream)" stroke-width="1.6" stroke-linecap="round"/>
        <path d="M4 16 L16 4" stroke="var(--cream)" stroke-width="1.6" stroke-linecap="round"/>
      </svg>
      ODOR<br>FREE
    </div>

    <p class="claim claim-natural">100% NATURAL</p>
    <p class="claim claim-organic">100% ORGANIC</p>

    <div class="brand-mark">
      <div class="brand-dot" role="img" aria-label="Brand emblem area"></div>
      <p class="brand-name">BRINDLE BONES<br>CHEWS</p>
    </div>

    <svg class="ingredients-heading" viewBox="0 0 480 30" aria-label="Only 3 ingredients">
      <text x="240" y="23" text-anchor="middle" font-family="Titan One, sans-serif" font-size="19"
            fill="var(--amber)" stroke="var(--ink)" stroke-width="3.5" stroke-linejoin="round" paint-order="stroke">ONLY 3 INGREDIENTS</text>
    </svg>

    <p class="ingredients-band">YAK MILK - LIME JUICE - HIMALAYAN SALT</p>
    <p class="net-weight">« SMALL » « MIN NET WT 200 G / 5 PCS »</p>
  </main>
</body>
</html>
```